HVAC company business card design

We need a business card design for a HVAC company. The design must look professional. Both sides will be used. The total data to be on the business card is
Name
Position
Email
Direct Phone/Moile Phone
Company Contacts /Address, Phone, Fax, web)
All data will be submit once the design is confirmed. For generic purposes use;
Cem Orkut
Managing Director
+902324418352 (Mobile)
4718 Sokak No: 9 KGTB Alsancak IZMIR TURKEY
Tel: +902324418352 Fax : +902324418359
www.ozkivra.com.tr

Target Market(s)

HVAC

Industry/Entity Type

Business

Contact Information for Business Card

The total data to be on the business card is
Name
Position
Email
Direct Phone/Moile Phone
Cem Orkut
Managing Director
+902324418352 (Mobile)
www.ozkivra.com.tr
The BC will use both sides of the card. The front will include the full logo and the details for the business card holder. The business card can be divided into vertical/horizontal or to a special shape. The common data like the company address/phone/fax should be indicated elsewehere. The back can contain some part or the whole logo and must contain the web address.

Font styles to use
Serif
Sans Serif

Colors
0355a3
cfdfed

Requirements
Should not have
• Please be careful with the fonts, it shouldnt be too small or too big and must not interfere with the logo fonts. If you need to use a curvy shape please do not use as the logo is already curvy or use the curves from the logo (if it looks good, otherwise forget it)
• We are not in favor of pictograms, only if they are perfect use them.

```html
<!DOCTYPE html>
<html lang="en">
<head>
<meta charset="utf-8">
<title>OZKIVRA business card</title>
<link href="https://fonts.googleapis.com/css2?family=Michroma&family=Open+Sans:wght@400;600&display=swap" rel="stylesheet">
<style>
  :root {
    --backdrop: #e4e4e6;
    --card-dark: #0b0b0d;
    --card-light: #ffffff;
    --brand-blue: #0355a3;
    --accent-blue: #3d7bd0;
    --slate: #333d58;
    --slate-muted: #4c5778;
    --grey-text: #6b6f78;
    --ice: #cfdfed;
  }
  * { margin: 0; padding: 0; box-sizing: border-box; }
  html, body { width: 1200px; height: 1200px; overflow: hidden; }
  body {
    background: var(--backdrop);
    font-family: "Open Sans", sans-serif;
    position: relative;
  }
  .card {
    position: absolute;
    left: 270px;
    width: 660px;
    height: 400px;
    border-radius: 26px;
    overflow: hidden;
  }
  .card--back { top: 110px; background: var(--card-dark); }
  .card--front { top: 630px; background: var(--card-light); box-shadow: 0 2px 10px rgba(0,0,0,0.08); }

  .brand { position: absolute; display: flex; align-items: center; gap: 22px; }
  .brand__dot { border-radius: 50%; background: var(--accent-blue); flex: none; }
  .brand__name { font-family: "Open Sans", sans-serif; font-weight: 600; letter-spacing: 2px; white-space: nowrap; }

  .card--back .brand { left: 120px; top: 160px; }
  .card--back .brand__dot { width: 96px; height: 96px; }
  .card--back .brand__name { font-size: 70px; color: var(--slate-muted); }
  .back__web {
    position: absolute; left: 0; right: 0; bottom: 58px;
    text-align: center; padding-left: 120px;
    font-size: 15px; letter-spacing: 5px; color: #3c4b7a;
  }

  .card--front .brand { left: 44px; top: 230px; gap: 16px; }
  .card--front .brand__dot { width: 74px; height: 74px; }
  .card--front .brand__name { font-size: 44px; color: var(--slate); }

  .holder { position: absolute; left: 380px; top: 62px; width: 260px; color: var(--slate); }
  .holder__name { font-family: "Michroma", sans-serif; font-size: 22px; color: var(--slate-muted); white-space: nowrap; }
  .holder__role { font-size: 12px; color: var(--grey-text); margin-top: 2px; }
  .holder__address { font-size: 14px; line-height: 1.45; margin-top: 22px; white-space: nowrap; }
  .contacts { list-style: none; margin-top: 14px; font-size: 14px; line-height: 1.45; }
  .contacts li { display: flex; align-items: center; gap: 10px; white-space: nowrap; }
  .contacts svg { width: 13px; height: 13px; fill: var(--brand-blue); flex: none; }
</style>
</head>
<body>
  <section class="card card--back" aria-label="Card back">
    <div class="brand">
      <span class="brand__dot"></span>
      <span class="brand__name">OZKIVRA</span>
    </div>
    <p class="back__web">www.ozkivra.com.tr</p>
  </section>

  <section class="card card--front" aria-label="Card front">
    <div class="brand">
      <span class="brand__dot"></span>
      <span class="brand__name">OZKIVRA</span>
    </div>
    <div class="holder">
      <h1 class="holder__name">Cem Orkut</h1>
      <p class="holder__role">Managing Director</p>
      <p class="holder__address">4718 Sokak No: 9/1 Kordonpark<br>B:47 KGTB Alsancak IZMIR<br>TURKEY</p>
      <ul class="contacts">
        <li><svg viewBox="0 0 12 12"><rect x="3" y="0" width="6" height="12" rx="1.2"/></svg>+90 532 418 63 27</li>
        <li><svg viewBox="0 0 12 12"><path d="M1 4c0-2 2-3 5-3s5 1 5 3l-2 1-1-2H4L3 5zM2 6h8v5H2z"/></svg>+90 232 441 83 52</li>
        <li><svg viewBox="0 0 12 12"><path d="M3 0h6v3H3zM1 4h10v5H9v3H3V9H1z"/></svg>+90 232 441 83 59</li>
        <li><svg viewBox="0 0 12 12"><path d="M0 2h12v1L6 7 0 3zM0 4.5l6 4 6-4V10H0z"/></svg>cem@ozkivra.com.tr</li>
        <li><svg viewBox="0 0 12 12"><circle cx="6" cy="6" r="6"/></svg>www.ozkivra.com.tr</li>
      </ul>
    </div>
  </section>
</body>
</html>
```